Business card design needed

We need a business card design for a new consulting business based in Melbourne called Harbourlight Advisory Consulting. Our tag line is 'Creating Impact Together'. We work with not for profits and Small - Medium Enterprises to provide advice and solutions around finance, governance, HR, IT and risk management. The idea around our organisation is to help charities and small businesses with their business foundations, so that they can spend more time focussing on their mission.
We have a logo designed already and would like the business card to use similar colours and themes - collaboration, having a conversation, creating impact. We would like the design to be eye catching but also convey professional credibility.
We would like a double sided card please.
Target Market(s)
CEOs and senior managers in charities and Small to Medium Enterprises
Industry/Entity Type
Business
Contact Information for Business Card
Business Name: Harbourlight Advisory Consulting
Staff Member: Danielle Okonkwo FCA
Title: Principal Consultant
Email address: danielle@harbourlightadvisory.example.com.au
Phone: 03 9871 2264
Mobile: 0418 246 730
Address: PO Box 87, Westvale VIC 3179
Web: www.harbourlightadvisory.example.com.au
Linked In: au.linkedin.com/in/danielleokonkwoha/
Look and feel
Each slider illustrates characteristics of the customer's brand and the style your logo design should communicate.

```html
<!DOCTYPE html>
<html lang="en">
<head>
<meta charset="utf-8">
<title>Harbourlight Advisory Consulting – Business Card</title>
<link rel="stylesheet" href="https://fonts.googleapis.com/css2?family=PT+Sans:wght@400;700&display=swap">
<style>
  :root {
    --card-yellow: #fddc14;
    --curl-yellow: #fff000;
    --band-black: #000000;
    --brand-purple: #6b2c91;
    --ink: #1a1a1a;
    --page: #ffffff;
  }
  * { margin: 0; padding: 0; box-sizing: border-box; }
  html, body {
    width: 1200px;
    height: 756px;
    overflow: hidden;
    background: var(--page);
  }
  .canvas {
    position: relative;
    width: 1200px;
    height: 756px;
    font-family: "PT Sans", "Myriad Pro", Arial, sans-serif;
    color: var(--ink);
  }
  .card {
    position: absolute;
    left: 62px;
    top: 62px;
    width: 1063px;
    height: 614px;
    background: var(--card-yellow);
    overflow: hidden;
  }
  .card-shapes {
    position: absolute;
    inset: 0;
    width: 1063px;
    height: 614px;
  }
  .card-shapes .top-band,
  .card-shapes .curl-back { fill: var(--band-black); }
  .card-shapes .curl-flap { fill: var(--curl-yellow); }
  .card-shapes .brand-dot { fill: var(--brand-purple); }

  .staff {
    position: absolute;
    left: 761px;
    top: 118px;
    font-size: 24px;
    line-height: 32px;
  }
  .brand-name {
    position: absolute;
    left: 113px;
    top: 328px;
    width: 620px;
    font-size: 35.5px;
    font-weight: 400;
    letter-spacing: 0.2px;
    color: var(--brand-purple);
    white-space: nowrap;
    text-transform: uppercase;
  }
  .contact {
    position: absolute;
    left: 0;
    top: 496px;
    width: 900px;
    text-align: center;
    font-size: 18.5px;
    line-height: 25px;
    white-space: nowrap;
  }
</style>
</head>
<body>
<div class="canvas">
  <div class="card">
    <svg class="card-shapes" viewBox="0 0 1063 614" aria-hidden="true">
      <polygon class="top-band" points="0,0 1063,0 1063,93"/>
      <polygon class="curl-back" points="1063,378 1063,614 883,614"/>
      <path class="curl-flap" d="M883,614 C888,540 886,460 893,400 C960,410 1020,398 1063,378 Z"/>
      <circle class="brand-dot" cx="251" cy="230" r="70"/>
    </svg>

    <div class="staff">
      <p class="staff-name">Danielle Okonkwo FCA</p>
      <p class="staff-title">Principal Consultant</p>
    </div>

    <p class="brand-name">Harbourlight Advisory Consulting</p>

    <div class="contact">
      <p class="contact-line">PO Box 87, Westvale VIC 3179, Phone: 03 9871 2264 Mobile: 0418 246 730</p>
      <p class="contact-line">E-mail: danielle@harbourlightadvisory.example.com.au</p>
      <p class="contact-line">Web: www.harbourlightadvisory.example.com.au&nbsp; Linked In: au.linkedin.com/in/danielleokonkwoha/</p>
    </div>
  </div>
</div>
</body>
</html>
```